Ember needs a new design we have an updated logo and want a high qualitative high end feel

feel and aesthetic should be high qualitative like the packaging in a zelvo or the qualatative weight/feel of an zelvo design. modern, elegant bold.probably just the ember logo on the backone vesion could be blue background white letter ... open to ideas
legal, insurance , medical, finance vantor 300
Information Technology
Serif

```html
<!DOCTYPE html>
<html lang="en">
<head>
<meta charset="utf-8">
<title>Ember Managed Services Group — Business Card</title>
<link href="https://fonts.googleapis.com/css2?family=Arimo:wght@400;700&display=swap" rel="stylesheet">
<style>
  :root {
    --backdrop: #3a3b3d;
    --paper: #f4f4f2;
    --navy: #16384c;
    --navy-deep: #0d2233;
    --navy-light: #1f4863;
    --grey-text: #8b8d8f;
    --grey-strong: #55585b;
    --white: #ffffff;
  }
  * { margin: 0; padding: 0; box-sizing: border-box; }
  html, body { width: 1200px; height: 900px; overflow: hidden; }
  body {
    background: var(--backdrop);
    font-family: "Arimo", Arial, sans-serif;
    position: relative;
  }
  .card {
    position: absolute;
    top: 118px;
    width: 380px;
    height: 665px;
    border-radius: 26px;
    box-shadow: 0 18px 40px rgba(0,0,0,.45);
  }
  .card-front { left: 170px; background: var(--paper); color: var(--navy); }
  .card-back {
    left: 650px;
    background: radial-gradient(ellipse at 45% 35%, var(--navy-light) 0%, var(--navy) 45%, var(--navy-deep) 100%);
    color: var(--white);
  }
  .person { position: absolute; top: 92px; left: 0; right: 0; text-align: center; }
  .person-name { font-size: 25px; font-weight: 700; letter-spacing: 1px; }
  .person-title { font-size: 15px; margin-top: 4px; color: #222; }

  .brand-name {
    position: absolute; left: 40px; right: 40px;
    text-align: center;
    font-size: 30px; font-weight: 700; line-height: 38px;
    color: currentColor;
  }
  .card-front .brand-name { top: 248px; }
  .card-back .brand-name { top: 278px; }

  .contact-icons {
    position: absolute; top: 392px; left: 0; right: 0;
    display: flex; justify-content: center; gap: 22px;
  }
  .contact-icon {
    width: 28px; height: 28px; border-radius: 50%;
    background: var(--navy); display: flex; align-items: center; justify-content: center;
  }
  .contact-icon svg { width: 15px; height: 15px; }

  .contact-lines {
    position: absolute; top: 444px; left: 0; right: 0; text-align: center;
    font-size: 17px; line-height: 30px; color: var(--grey-text);
  }
  .contact-lines strong { color: var(--grey-strong); }
  .divider { width: 20px; height: 4px; background: var(--navy); margin: 14px auto 16px; }
  .address { font-size: 18px; line-height: 24px; font-weight: 700; color: var(--navy); }

  .back-url { position: absolute; bottom: 92px; right: 34px; font-size: 16px; letter-spacing: .5px; }
</style>
</head>
<body>
  <section class="card card-front">
    <div class="person">
      <p class="person-name">DANA WHITLOW</p>
      <p class="person-title">Founder/CEO</p>
    </div>
    <p class="brand-name">Ember Managed<br>Services Group, Inc.</p>
    <div class="contact-icons">
      <span class="contact-icon" aria-label="Phone">
        <svg viewBox="0 0 16 16"><path fill="#fff" d="M3.5 1.5l2.5 2.7-1.3 1.6c.9 2 2.4 3.6 4.5 4.5l1.6-1.3 2.7 2.5-1.6 2.2C7 13.3 2.7 9 1.3 3.1z"/></svg>
      </span>
      <span class="contact-icon" aria-label="Email">
        <svg viewBox="0 0 16 16"><rect x="2" y="4" width="12" height="8.5" fill="#fff"/><path d="M2 4l6 5 6-5" fill="none" stroke="#16384c" stroke-width="1.2"/></svg>
      </span>
      <span class="contact-icon" aria-label="Website">
        <svg viewBox="0 0 16 16"><g fill="none" stroke="#fff" stroke-width="1.8"><rect x="2.5" y="6" width="6" height="4" rx="2" transform="rotate(-45 5.5 8)"/><rect x="7.5" y="6" width="6" height="4" rx="2" transform="rotate(-45 10.5 8)"/></g></svg>
      </span>
    </div>
    <div class="contact-lines">
      <p>(555) 214-0187</p>
      <p>help@embermsg.com</p>
      <p>www.<strong>embermsg</strong>.com</p>
      <div class="divider"></div>
      <p class="address">480 Harbor Ln Suite 12<br>Fairview, VA 20117</p>
    </div>
  </section>

  <section class="card card-back">
    <p class="brand-name">Ember Managed<br>Services Group, Inc.</p>
    <p class="back-url">www.embermsg.com</p>
  </section>
</body>
</html>
```